Velmor Glazing

Modern glazing company specializing in commercial fit outs, pool fencing, frameless showers and glass splash backs, im after a very young/modern logo, it doesnt have to be revelent to glazing and a classy "boss like" design for the card. thank you in advanced

im thinking carbon fiber back ground or something along that line with bright orange wording or something maybe, open to suggestions 

Fencing

company name, name, phone and products

```html
<!DOCTYPE html>
<html lang="en">
<head>
<meta charset="utf-8">
<title>Velmor Glazing – Business Card</title>
<link href="https://fonts.googleapis.com/css2?family=Merienda:wght@700&display=swap" rel="stylesheet">
<style>
  :root {
    --page: #ffffff;
    --navy-deep: #1c2270;
    --navy: #2e3a9a;
    --navy-light: #5a6bc0;
    --silver-dark: #8a9aa4;
    --silver: #c3ced4;
    --silver-light: #eef2f4;
    --ink: #111111;
    --white: #ffffff;
  }
  * { margin: 0; padding: 0; box-sizing: border-box; }
  html, body {
    width: 1013px;
    height: 1200px;
    overflow: hidden;
    background: var(--page);
  }
  .canvas {
    position: relative;
    width: 1013px;
    height: 1200px;
    font-family: "Merienda", cursive;
    font-weight: 700;
  }
  .card {
    position: absolute;
    left: 155px;
    width: 773px;
    height: 407px;
    overflow: hidden;
  }
  .card--front { top: 155px; }
  .card--back { top: 624px; }
  .card__art {
    position: absolute;
    inset: 0;
    width: 100%;
    height: 100%;
  }
  .brand {
    position: absolute;
    line-height: 1;
  }
  .brand__line { display: block; }
  .card--front .brand {
    left: 60px;
    top: 44px;
    color: var(--white);
    font-size: 34px;
  }
  .card--front .brand__line--second { margin-left: 60px; margin-top: 10px; }
  .card--back .brand {
    left: 300px;
    top: 62px;
    color: var(--ink);
    font-size: 54px;
  }
  .card--back .brand__line--second { margin-left: 100px; margin-top: 14px; }
  .brand-dot {
    position: absolute;
    left: 196px;
    top: 66px;
    width: 84px;
    height: 84px;
    border-radius: 50%;
    background: var(--ink);
  }
  .contact {
    position: absolute;
    right: 102px;
    top: 158px;
    text-align: right;
    color: var(--ink);
  }
  .contact__name { font-size: 56px; line-height: 1.1; }
  .contact__phone { font-size: 24px; margin-top: 22px; }
  .contact__email { font-size: 20px; margin-top: 12px; }
  .services {
    position: absolute;
    left: 110px;
    top: 204px;
    width: 240px;
    list-style: none;
    text-align: center;
    color: var(--white);
    font-size: 17px;
    line-height: 47px;
  }
</style>
</head>
<body>
<main class="canvas">

  <section class="card card--front" aria-label="Business card front">
    <svg class="card__art" viewBox="0 0 773 407" aria-hidden="true">
      <defs>
        <linearGradient id="front-silver" x1="0" y1="0" x2="1" y2="1">
          <stop offset="0" stop-color="var(--silver-dark)"/>
          <stop offset="0.45" stop-color="var(--silver-light)"/>
          <stop offset="1" stop-color="var(--silver)"/>
        </linearGradient>
        <linearGradient id="front-navy" x1="0" y1="0" x2="1" y2="0">
          <stop offset="0" stop-color="var(--navy-deep)"/>
          <stop offset="0.5" stop-color="var(--navy-light)"/>
          <stop offset="0.7" stop-color="var(--navy)"/>
          <stop offset="1" stop-color="var(--navy-deep)"/>
        </linearGradient>
      </defs>
      <rect width="773" height="407" fill="url(#front-silver)"/>
      <path d="M0 0 H773 V78 C560 90 420 110 300 165 C190 215 90 250 0 262 Z" fill="url(#front-navy)"/>
      <path d="M0 290 C90 278 190 240 300 190 C420 135 560 112 773 100" fill="none" stroke="var(--navy-light)" stroke-width="22" opacity="0.45"/>
      <path d="M0 274 C90 262 190 226 300 177 C420 122 560 99 773 88" fill="none" stroke="var(--white)" stroke-width="16"/>
    </svg>
    <div class="brand">
      <span class="brand__line">Velmor</span>
      <span class="brand__line brand__line--second">Glazing</span>
    </div>
    <div class="contact">
      <p class="contact__name">Dale Archer</p>
      <p class="contact__phone">902.555.0147</p>
      <p class="contact__email">dalearcher@mailbox.com</p>
    </div>
  </section>

  <section class="card card--back" aria-label="Business card back">
    <svg class="card__art" viewBox="0 0 773 407" aria-hidden="true">
      <defs>
        <linearGradient id="back-silver" x1="0" y1="0" x2="1" y2="1">
          <stop offset="0" stop-color="var(--silver-dark)"/>
          <stop offset="0.55" stop-color="var(--silver-light)"/>
          <stop offset="1" stop-color="var(--silver)"/>
        </linearGradient>
        <linearGradient id="back-navy" x1="0" y1="0" x2="1" y2="0">
          <stop offset="0" stop-color="var(--navy)"/>
          <stop offset="1" stop-color="var(--navy-deep)"/>
        </linearGradient>
      </defs>
      <rect width="773" height="407" fill="url(#back-silver)"/>
      <path d="M520 407 C610 360 690 330 773 312 V407 Z" fill="url(#back-navy)"/>
      <path d="M500 407 C600 352 685 322 773 300" fill="none" stroke="var(--white)" stroke-width="12"/>
    </svg>
    <span class="brand-dot" aria-hidden="true"></span>
    <div class="brand">
      <span class="brand__line">Velmor</span>
      <span class="brand__line brand__line--second">Glazing</span>
    </div>
    <ul class="services">
      <li>commercial fit outs</li>
      <li>pool fencing</li>
      <li>frameless showers</li>
      <li>glass splash backs</li>
    </ul>
  </section>

</main>
</body>
</html>
```